Tarrowind High School Association Website New Design

We require a fresh new website design for the Tarrowind High School Old Boys Association. The association is a non-for-profit and as such we like the site to reflect the ethos.
We require a design that uses responsive design techniques, so to allow the site to shift between mobile, tablet and desktop spaces and maintain elements in the site.
We would like a landing/home page design, and also an inner news/article based design included.
We want the site to appeal to a broad market of both the old guard members but also to bring on board the new social savey younger members.
The site needs to have a modern take on a professional yet fresh and opulent/elegant look.
A site that we like influences from is http://www.quennaval-lodge.com/ we especially like the navigation look and feel.
The site needs to be clean and simple to find information and navigate and as such would like the site design elements to reflect this in its layout and element interplay.
This site will act as an information gateway for the member's, but also offer abilities to purchase memberships, get information on up coming events and purchase tickets to these events, and interact with the members on the site.
Hi All designers,
The client has now agreed to make the project funding guaranteed, so I hope to see some great designs from you.
Thanks
Sorry all, I hadn't uploaded the logo, has now been uploaded.
Hi all designers, please don't let the wireframe layout include restrict your design freedom on the page layout. We included this to give you a feel for the elements wanted in the site, but not to push you to have them all in that arrangement. Feel free to move around or remove parts of to make better use of the space.
Also this site is for ex-students who are members of an association linked to the school, and not for the school itself, so your designs need to lean towards a member, events and reunions type site design.
After a review today, client now requires that the sites Events need special consideration. Want to see in a prominent position on the landing page area a good area to showcase the upcoming events. Please take this into consideration in your future design layouts.
Hi All Designers, I appreciate all the new and current designs, and sorry a bit behind on the feedback, have been a bit swamped on my own workload, I will give feedback to you all, and will maybe look at an extension of the deadline if need be, as to also allow the clients to look over designs.
Thanks
Reason: Extending the project deadline to allow more feedback to be provider to all designers, to allow review by clients and the feedback through myself.
Reason: Client was un-available for comment, and want them to be able to give feedback to designers for last round updates.
Reason: Sorry all, client has been overseas, and will only be back next week, so need to extend the deadline to allow for client input next week.
Reason: Sorry client has be delayed overseas, so when be needing to work through the designs next week to allow full ability to give all designs due recognition.
Reason: Waiting for client to review designs.
Target Market(s)
Professionals from all varity of job types
Industry/Entity Type
Events
Requirements
Must have
- Please use the attached Logo in the design and look to use the current colour pallet as much as possible, but open to colour and pallet additions or amendments.
Must have a “hero” header image scroller for ability to showcase upcoming events and other items (Required for home/landing pages, could be amended or removed on inner pages).
Should look to follow the include wire frame layout concept as a good conception starting point - but do not limit to just this layout, use design discretion.
Include prominently positioned events area in layout for upcoming events to push the events heavy aspect of the site.
Should include icons/link abilities to access social sites and applications. Ie Plumvine etc.
Nice to have
- A modern look with an edge to it.
Creative use of the sites colour pallet and site elements.
Should not have
- should not be a copy of the wireframe with colour added

```html
<!DOCTYPE html>
<html lang="en">
<head>
<meta charset="utf-8">
<title>Tarrowind High School Old Boys Association</title>
<link rel="stylesheet" href="https://fonts.googleapis.com/css2?family=Ubuntu:wght@400;500;700&family=Roboto+Condensed:wght@400;700&family=Arimo:wght@400;700&display=swap">
<style>
:root{
  --green-dark:#0b4a2c;
  --green:#13693f;
  --green-link:#1b5e3a;
  --crimson:#a3123a;
  --crimson-dark:#7d0c2b;
  --orange:#e5501b;
  --nav-blue:#c7dcef;
  --text:#2a2a2a;
  --grey-bg:#dcdcdc;
  --panel:#ededed;
  --footer:#050505;
  --footer-green:#1f8a5a;
}
*{box-sizing:border-box;margin:0;padding:0}
html,body{width:1029px;height:1200px;overflow:hidden}
body{position:relative;background:#fff;font-family:"Ubuntu",sans-serif;color:var(--text)}
a{color:inherit}
.abs{position:absolute}

/* header */
.masthead{left:0;top:0;width:1029px;height:125px;background:linear-gradient(#1d7a4a,var(--green-dark) 85%)}
.brand-tab{left:105px;top:0;width:165px;height:83px;background:#fff;border-radius:0 0 14px 14px;box-shadow:0 3px 6px rgba(0,0,0,.35);display:flex;align-items:center;justify-content:center;gap:7px}
.brand-mark{width:10px;height:10px;background:var(--green)}
.brand-name{font:400 15px "Arimo",sans-serif;color:#333}
.site-title{left:310px;top:35px;font:400 21px "Roboto Condensed",sans-serif;color:#fff;text-shadow:0 1px 2px rgba(0,0,0,.5)}
.search{left:694px;top:37px;width:170px;height:23px;border-radius:4px;background:linear-gradient(#9ccdb2,#7fb89a);border:1px solid #5c9677}
.search-btn{left:868px;top:37px;width:53px;height:23px;border-radius:4px;background:linear-gradient(#f46a2e,#d43c0f);color:#fff;font:400 11px "Arimo",sans-serif;display:flex;align-items:center;justify-content:center}

.main-nav{left:106px;top:91px;width:816px;height:34px;display:flex;background:linear-gradient(#d6e6f4,var(--nav-blue))}
.main-nav a{display:flex;align-items:center;justify-content:center;font:400 12.5px "Arimo",sans-serif;color:#111;text-decoration:none;border-right:1px solid #e9f2fa}
.main-nav a:last-child{border-right:0}

.hero-band{left:0;top:125px;width:1029px;height:350px;background:linear-gradient(#e8e8e8,#fff)}
.hero{left:106px;top:125px;width:816px;height:329px;background:linear-gradient(#a9cdea 0%,#d9e8f3 30%,#7a3a2c 48%,#6e3528 62%,#6a8d3c 72%,#4d6b2a 100%)}
.hero-dots{left:137px;top:435px;display:flex;gap:5px}
.hero-dots span{width:10px;height:10px;border-radius:50%;background:#b9b9b9}
.hero-dots span:first-child{background:#fff}

/* content */
.content-band{left:0;top:475px;width:1029px;height:499px;background:var(--grey-bg)}
.kicker{font:700 12px "Ubuntu",sans-serif;color:#8a8a8a;letter-spacing:.3px;line-height:1}
.section-title{font:700 22px "Ubuntu",sans-serif;color:var(--crimson);line-height:1.05}
.section-title b{color:var(--green)}
.rule{height:2px;background:linear-gradient(90deg,transparent,#b5b5b5 20%,#b5b5b5 80%,transparent)}

.events-panel{left:105px;top:485px;width:265px;height:475px;background:linear-gradient(#fbfbfb,var(--panel) 12%);border:2px solid #fff;border-radius:10px;box-shadow:0 2px 4px rgba(0,0,0,.2)}
.scroll-track{width:7px;background:#e4e4e4}
.scroll-thumb{width:7px;background:#9c9c9c}

.item-title{font:400 12.5px "Ubuntu",sans-serif;color:var(--green-link);text-decoration:underline}
.item-date{font:400 10.5px "Ubuntu",sans-serif;color:var(--crimson)}
.item-body{font:400 10.5px/15.4px "Ubuntu",sans-serif;color:#222}
.item-body a,.link-red{color:var(--crimson)}
.thumb{border:2px solid #fff;box-shadow:0 0 2px rgba(0,0,0,.35)}
.divider{height:1px;background:#a9a9a9}

.about-text{font:400 10px/20.6px "Ubuntu",sans-serif;color:#333}
.more-line{height:1px;background:#a5a5a5}
.more-btn{width:101px;height:22px;background:linear-gradient(#2b8558,#0f5a35);color:#fff;font:400 12.5px "Roboto Condensed",sans-serif;display:flex;align-items:center;justify-content:center;box-shadow:0 1px 2px rgba(0,0,0,.3)}

/* footer */
.footer{left:0;top:974px;width:1029px;height:226px;background:var(--footer)}
.foot-head{font:400 15.5px "Arimo",sans-serif;color:var(--footer-green)}
.foot-links{list-style:none}
.foot-links li{font:400 12.5px "Arimo",sans-serif;color:#fff;height:24px;display:flex;align-items:center;gap:14px}
.foot-links li::before{content:"";border-left:7px solid var(--crimson);border-top:5px solid transparent;border-bottom:5px solid transparent}
.contact-list{list-style:none}
.contact-list li{font:400 12.5px "Arimo",sans-serif;color:#ddd;height:24px}
.social{display:flex;gap:10px}
.social a{display:flex;align-items:center;gap:5px;font:400 12px "Arimo",sans-serif;color:#fff;text-decoration:none}
.social i{width:14px;height:14px;display:block}
.newsletter{left:678px;top:1119px;width:226px;height:36px;background:#fff;border:1px solid #aaa;border-radius:3px}
.newsletter span{position:absolute;left:10px;top:11px;font:400 10.5px "Roboto Condensed",sans-serif;color:#999}
.join-btn{right:4px;top:3px;width:49px;height:28px;border-radius:3px;background:linear-gradient(#c0153f,var(--crimson-dark));color:#fff;font:400 12.5px "Arimo",sans-serif;display:flex;align-items:center;justify-content:center}
</style>
</head>
<body>

<header>
  <div class="abs masthead"></div>
  <div class="abs brand-tab"><span class="brand-mark"></span><span class="brand-name">Tarrowind Old Boys</span></div>
  <div class="abs site-title">Tarrowind High School Old Boys’ Association</div>
  <div class="abs search" aria-label="Search field"></div>
  <div class="abs search-btn">SEARCH</div>
  <nav class="abs main-nav">
    <a style="width:118px">HOME</a>
    <a style="width:120px">NEWS</a>
    <a style="width:132px">EVENTS</a>
    <a style="width:138px">PHOTOS</a>
    <a style="width:164px">MEMBERSHIP</a>
    <a style="width:144px">CONTACT</a>
  </nav>
</header>

<div class="abs hero-band"></div>
<div class="abs hero" role="img" aria-label="Photo of the red-brick school building on a grassy hill under a blue sky"></div>
<div class="abs hero-dots"><span></span><span></span><span></span><span></span></div>

<main>
  <div class="abs content-band"></div>

  <section class="abs events-panel">
    <div class="abs" style="left:12px;top:11px">
      <div class="kicker">UPCOMING</div>
      <div class="section-title">EVENTS <b>!!</b></div>
    </div>
    <div class="abs rule" style="left:8px;top:55px;width:245px"></div>
    <div class="abs scroll-track" style="left:251px;top:70px;height:385px"></div>
    <div class="abs scroll-thumb" style="left:251px;top:70px;height:112px"></div>

    <div class="abs" style="left:19px;top:74px;width:225px">
      <div class="item-title">New Golf Day: The Callow Trophy</div>
      <div class="item-date">Monday 24 September 2012</div>
    </div>
    <div class="abs thumb" role="img" aria-label="Golf ball on a tee with a club" style="left:9px;top:110px;width:75px;height:66px;background:linear-gradient(#8ec3ee,#b6dcf2 45%,#5aa13a 55%,#3f7d26)"></div>
    <div class="abs item-body" style="left:93px;top:107px;width:152px">Due to player demand we are delighted to announce the THSOBA Callow Trophy Golf Day on Monday 24 September 2012 at Fernhill Golf Club, <a href="#">More</a></div>
    <div class="abs divider" style="left:9px;top:208px;width:236px"></div>

    <div class="abs" style="left:19px;top:213px;width:225px">
      <div class="item-title">Kestrel Bay Luncheon: Mr Alan Brecker</div>
      <div class="item-date">Wednesday 19 September 2012</div>
    </div>
    <div class="abs thumb" role="img" aria-label="Microphone in front of a seated audience" style="left:9px;top:249px;width:75px;height:66px;background:linear-gradient(135deg,#b0382a,#6a1d14 60%,#2b0c08)"></div>
    <div class="abs item-body" style="left:93px;top:246px;width:152px">The 5th of our Kestrel Bay luncheons at the Kestrel Bay Club (74 Ashby Street) has now been locked in to Wednesday 19 September 2012 at 12.30pm for a 1.00pm sit down. <a href="#">More</a></div>
    <div class="abs divider" style="left:9px;top:349px;width:236px"></div>

    <div class="abs" style="left:19px;top:354px;width:225px">
      <div class="item-title">THSOBA Winemaker Dinner Series</div>
      <div class="item-date">Tuesday 14 August 2012</div>
    </div>
    <div class="abs thumb" role="img" aria-label="Plated dinner with glasses of red wine" style="left:9px;top:403px;width:75px;height:65px;background:linear-gradient(#3a2a22,#6b4a36 50%,#e8e2d8)"></div>
    <a class="abs link-red" style="left:93px;top:406px;font:400 10.5px Ubuntu,sans-serif;text-decoration:underline">Online bookings</a>
  </section>

  <section>
    <div class="abs" style="left:392px;top:496px">
      <div class="kicker">LATEST</div>
      <div class="section-title">NEWS <b>!!</b></div>
    </div>
    <div class="abs rule" style="left:388px;top:540px;width:250px"></div>
    <div class="abs scroll-track" style="left:631px;top:557px;height:387px;background:#cfcfcf"></div>
    <div class="abs scroll-thumb" style="left:631px;top:557px;height:114px"></div>

    <div class="abs" style="left:396px;top:551px;width:228px">
      <div class="item-title">August Luncheon: Red Silk Steps</div>
      <div class="item-date">Monday 24 September 2012</div>
      <div class="item-body" style="margin-top:8px">Due to player demand we are delighted to announce the THSOBA Callow Trophy Golf Day on Monday 24 September 2012 at Fernhill Golf Club, <a href="#">More</a></div>
    </div>
    <div class="abs divider" style="left:389px;top:663px;width:235px"></div>

    <div class="abs" style="left:396px;top:674px;width:228px">
      <div class="item-title">Medicine &amp; Health Sciences Scholarship in 2012</div>
      <div class="item-date">Wednesday 19 September 2012</div>
      <div class="item-body" style="margin-top:8px">The ocked in to Wednesday 19 September 2012 at 12.30pm for a 1.00pm sit down. <a href="#">More</a></div>
    </div>
    <div class="abs divider" style="left:389px;top:770px;width:235px"></div>

    <div class="abs" style="left:396px;top:781px;width:228px">
      <div class="item-title">THS International Night</div>
      <div class="item-date">Tuesday 14 August 2012</div>
      <div class="item-body" style="margin-top:8px">Guest speaker is Mr Alan Brecker, Principal THS. He will bring all patrons up-to-date about happenings at our great school. All Kestrel Bay area Old Boys and guests are most welcome. <a href="#">More</a></div>
    </div>
    <div class="abs divider" style="left:389px;top:893px;width:235px"></div>

    <div class="abs" style="left:396px;top:905px;width:228px">
      <div class="item-title">THSOBA Mid-Year Report Card</div>
      <div class="item-date">Tuesday 14 August 2012</div>
    </div>
  </section>

  <section>
    <div class="abs" style="left:667px;top:496px">
      <div class="kicker">WHO WE ARE</div>
      <div class="section-title">MEET US <b>!!</b></div>
    </div>
    <div class="abs rule" style="left:665px;top:542px;width:215px"></div>
    <div class="abs thumb" role="img" aria-label="Members gathered in a hall listening to a speaker" style="left:660px;top:558px;width:110px;height:98px;background:linear-gradient(#7a5b8c,#3b2c3a 45%,#1c1a1c)"></div>
    <div class="abs about-text" style="left:779px;top:556px;width:130px">Nulla ut elit nunc, sed porka justo.Etlima none fasilimpa. Etrika egit isomiu posture postegeus nuhosed velit. Mobile frideem technique...</div>
    <div class="abs more-line" style="left:667px;top:684px;width:237px"></div>
    <div class="abs more-btn" style="left:731px;top:673px">More</div>

    <div class="abs" style="left:672px;top:743px">
      <div class="kicker">WHAT WE DO</div>
      <div class="section-title">JOIN US <b>!!</b></div>
    </div>
    <div class="abs rule" style="left:668px;top:788px;width:212px"></div>
    <div class="abs thumb" role="img" aria-label="Student band performing under a glass roof" style="left:660px;top:803px;width:110px;height:97px;background:linear-gradient(#7fa08a,#4a5a48 45%,#2a221c)"></div>
    <div class="abs about-text" style="left:779px;top:800px;width:130px">Nulla ut elit nunc, sed porka justo.Etlima none fasilimpa. Etrika egit isomiu posture postegeus nuhosed velit. Mobile frideem technique...</div>
    <div class="abs more-line" style="left:667px;top:934px;width:237px"></div>
    <div class="abs more-btn" style="left:733px;top:923px">More</div>
  </section>
</main>

<footer>
  <div class="abs footer"></div>
  <div class="abs" style="left:100px;top:1000px">
    <div class="foot-head">HEADING TO GO HERE</div>
    <ul class="foot-links" style="margin-top:12px;margin-left:4px">
      <li>payment</li><li>about us</li><li>contact us</li><li>links</li>
    </ul>
  </div>
  <div class="abs" style="left:389px;top:1000px">
    <div class="foot-head">CONTACT US</div>
    <ul class="contact-list" style="margin-top:14px">
      <li>P &nbsp;I &nbsp;(03) 9000 4170</li>
      <li>E &nbsp;I &nbsp;info@thsoba-mail.org</li>
      <li>W I &nbsp;www.thsoba-site.org.au</li>
      <li>P &nbsp;I &nbsp;53 Your Street to go here</li>
    </ul>
  </div>
  <div class="abs" style="left:678px;top:993px">
    <div class="foot-head">GET SOCIAL</div>
    <div class="social" style="margin-top:32px">
      <a><i style="background:#3b5b9a"></i>Plumvine</a>
      <a><i style="background:#f08a1c"></i>RSS</a>
      <a><i style="background:#4fb9e3"></i>Chirpline</a>
    </div>
  </div>
  <div class="abs foot-head" style="left:678px;top:1092px">NEWSLETTER</div>
  <div class="abs newsletter"><span>Enter your email</span><div class="abs join-btn">Join</div></div>
</footer>

</body>
</html>
```